Redesign of iOS App Moriva Tutor

Redesign of existing App Moriva Tutor, an app that helps learning Japanese Kanjis, Hiragana, Katakana.

The functionallity should remain the same as today: the app is free, you may download it at the app store. But: I like the design of my other apps better ;)

Target Market(s)

Students learning Japanese

Industry/Entity Type

Teacher

Font styles to use
Sans Serif

Requirements
Must have
• Moriva Tutor has 7 main screens, all screens has to be designed for iPhone and iPad: Main, Settings, Reading Tests, Writing Tests, Game, Paper Mode, Search
Nice to have
• I like the logo as it is today

```html
<!DOCTYPE html>
<html lang="en">
<head>
<meta charset="utf-8">
<title>Moriva Tutor – App Screens</title>
<link rel="stylesheet" href="https://fonts.googleapis.com/css2?family=Open+Sans:wght@300;400;600;700&family=Noto+Sans+JP:wght@300;400;700;900&display=swap">
<style>
:root{
  --bg:#8c8c8c;
  --screen:#f2f2f2;
  --card:#ffffff;
  --ink:#1e1e1e;
  --text:#333333;
  --muted:#9a9a9a;
  --faint:#d4d4d4;
  --line:#e4e4e4;
  --green:#1fbf8f;
  --blue:#2f8ff0;
  --red:#ee4b37;
  --grey-cell:#8a8a8a;
  --yellow:#f2b705;
  --yellow-faint:#f6dc8c;
  --olive:#9ab83a;
  --orange:#f59c2a;
  --purple:#5a3fbf;
  --seg:#e2e2e2;
}
*{box-sizing:border-box;margin:0;padding:0}
html,body{width:1159px;height:1200px;overflow:hidden;background:var(--bg)}
body{position:relative;font-family:"Open Sans",sans-serif;color:var(--text)}
.jp{font-family:"Noto Sans JP",sans-serif}
.screen{position:absolute;width:250px;height:444px;background:var(--screen);overflow:hidden}
.abs{position:absolute}
.status{position:absolute;left:0;top:0;width:100%;height:18px;background:#fff;display:flex;justify-content:space-between;align-items:center;padding:0 6px;font-size:6.5px;color:#aaa}
.status .bat{display:inline-block;width:13px;height:5px;background:#bbb;margin-left:3px;vertical-align:middle}
.bottombar{position:absolute;left:0;bottom:0;width:100%;height:34px;display:flex;align-items:center;padding:0 10px;font-size:8px;font-weight:600;color:#555}
.burger{width:11px;height:8px;border-top:1.2px solid #aaa;border-bottom:1.2px solid #aaa;position:relative}
.burger::after{content:"";position:absolute;left:0;right:0;top:2.2px;border-top:1.2px solid #aaa}
.score{position:absolute;top:36px;width:100%;display:flex;justify-content:space-around;text-align:center}
.score .lab{font-size:7px;font-weight:700;letter-spacing:.2px}
.score .num{font-size:15px;font-weight:300;line-height:20px}
.score .sub{font-size:6.5px}
.c-green{color:var(--green)}.c-red{color:var(--red)}.c-blue{color:var(--blue)}.c-yellow{color:var(--yellow)}.c-dark{color:var(--ink)}
.card{position:absolute;left:10px;width:230px;background:var(--card);box-shadow:0 1px 0 #ddd,0 3px 0 #fff,0 4px 0 #ddd,0 6px 0 #fff,0 7px 0 #ddd}
.star{position:absolute;font-size:12px;color:#ccc}
.board{position:absolute;border:1px solid var(--line);background:
  linear-gradient(var(--line),var(--line)) center/100% 1px no-repeat,
  linear-gradient(var(--line),var(--line)) center/1px 100% no-repeat}
.big{position:absolute;inset:0;display:flex;align-items:center;justify-content:center;font-family:"Noto Sans JP",sans-serif;font-weight:900;color:#000}

/* main */
.tabs{position:absolute;top:28px;left:0;width:100%;display:flex;justify-content:space-around;padding:0 10px;font-size:8px;color:#999}
.tabs .on{color:var(--ink);font-weight:700;border-bottom:1.5px solid var(--ink);padding-bottom:4px}
.tests-head{position:absolute;top:74px;left:8px;right:8px;height:14px;font-size:6.5px;color:#444;border-bottom:1px solid var(--line)}
.tests-head span{position:absolute;top:0}
.row{position:absolute;left:8px;right:8px;height:30px;border-bottom:1px solid var(--line);display:flex;align-items:center;font-size:7.5px;font-weight:700;color:var(--ink)}
.cell{position:absolute;top:8px;width:28px;height:13px;color:#fff;font-size:6.5px;font-weight:600;text-align:right;padding-right:3px;line-height:13px}
.cell.g{background:var(--grey-cell);left:112px}.cell.gr{background:var(--green);left:142px}.cell.b{background:var(--blue);left:172px}.cell.r{background:var(--red);left:202px}
.tool{display:flex;flex-direction:column;align-items:center;font-size:5.5px;color:#aaa;font-weight:400;width:38px;gap:2px}

/* game */
.gamegrid{position:absolute;left:20px;top:145px;width:210px;height:210px;display:grid;grid-template-columns:repeat(3,1fr);grid-template-rows:repeat(3,1fr)}
.gamegrid div{display:flex;align-items:center;justify-content:center;font-family:"Noto Sans JP",sans-serif;font-size:17px;color:var(--ink);border-right:1px solid var(--line);border-bottom:1px solid var(--line)}
.gamegrid div:nth-child(3n){border-right:0}.gamegrid div:nth-child(n+7){border-bottom:0}
.gamegrid .off{color:#d8d8d8}
.coin{width:34px;height:34px;border-radius:50%;border:1.5px solid var(--yellow);display:flex;flex-direction:column;align-items:center;justify-content:center;font-size:5.5px;font-weight:700;color:#444;line-height:7px;text-align:center}
.coin.off{border-color:var(--yellow-faint);color:#bbb}

/* reading */
.answers{position:absolute;left:10px;top:70px;width:210px;height:210px;display:grid;grid-template-columns:repeat(3,1fr);grid-template-rows:repeat(3,1fr)}
.answers div{display:flex;flex-direction:column;align-items:center;justify-content:center;font-size:8.5px;color:#333;border-right:1px solid var(--line);border-bottom:1px solid var(--line)}
.answers div:nth-child(3n){border-right:0}.answers div:nth-child(n+7){border-bottom:0}
.answers .bad{background:var(--red);color:#fff}.answers .good{background:var(--green);color:#fff;font-weight:700}
.answers b{font-size:9px;line-height:10px}

/* search */
.entry{position:absolute;left:0;width:100%;height:48px;border-bottom:1px solid var(--line);background:#fff}
.entry .kana{position:absolute;left:10px;top:8px;font-size:22px;color:var(--ink);font-family:"Noto Sans JP",sans-serif;font-weight:300}
.entry .rom{position:absolute;left:42px;top:12px;font-size:7px}
.entry .dots{position:absolute;left:42px;top:25px;font-size:7px;color:#999;letter-spacing:-1px}
.entry .type{position:absolute;left:90px;top:18px;font-size:8px}
.entry .lvl{position:absolute;left:206px;top:18px;font-size:8px}
.entry .st{position:absolute;left:222px;top:13px;font-size:15px;color:#ccc}
.popup{position:absolute;left:100px;top:245px;width:144px;height:168px;background:#fff;box-shadow:0 0 4px rgba(0,0,0,.25);padding:10px}
.popup .btn{border:1px solid #bbb;height:22px;font-size:6.5px;font-weight:700;display:flex;align-items:center;justify-content:center;color:#333}
.popup .lab{font-size:6.5px;margin:14px 0 6px;color:#444}
.dot{width:22px;height:22px;border-radius:50%;display:inline-block;margin-right:5px}

/* settings */
.set-lab{position:absolute;left:10px;font-size:8px;color:#333}
.seg{position:absolute;left:10px;right:10px;height:22px;display:flex;gap:2px}
.seg span{flex:1;background:var(--seg);color:#aaa;font-size:6.5px;font-weight:600;display:flex;align-items:center;justify-content:center;letter-spacing:.3px}
.seg .sel{background:#fff;color:var(--ink);font-weight:700}

/* detail */
.hdr{position:absolute;top:18px;left:0;width:100%;height:34px;background:#fff;display:flex;align-items:center;justify-content:center;font-size:7.5px;color:#777;letter-spacing:.3px}
.drow{position:absolute;left:0;width:100%;background:#fff;border-bottom:1px solid var(--line);font-size:8.5px;color:var(--ink)}
.drow span{position:absolute}
.sect{position:absolute;left:10px;font-size:7.5px;color:#aaa}
.red{color:var(--red)}
</style>
</head>
<body>

<!-- 1 Main -->
<section class="screen" style="left:30px;top:110px;background:#fff">
  <div class="status"><span>●●●●○ Carrier</span><span>5:30PM</span><span>100%<i class="bat"></i></span></div>
  <nav class="tabs"><span>K</span><span class="on">N5</span><span>N4</span><span>N3</span><span>N2</span><span>N1</span><span>★</span></nav>
  <div class="tests-head"><span style="left:0">TESTS</span><span style="left:122px">▶</span><span style="left:152px;color:var(--green)">✔</span><span style="left:182px;color:var(--blue)">○</span><span style="left:212px;color:var(--red)">✕</span></div>
  <div class="row" style="top:88px">Kanji ⇒ Meaning (103)<i class="cell g">103</i><i class="cell gr">0</i><i class="cell b">0</i><i class="cell r">0</i></div>
  <div class="row" style="top:118px">Meaning ⇒ Kanji (103)<i class="cell g">103</i><i class="cell gr">0</i><i class="cell b">0</i><i class="cell r">0</i></div>
  <div class="row" style="top:148px">Kanji ⇒ On (103)<i class="cell g">103</i><i class="cell gr">0</i><i class="cell b">0</i><i class="cell r">0</i></div>
  <div class="row" style="top:178px">On ⇒ Kanji (103)<i class="cell g">103</i><i class="cell gr">0</i><i class="cell b">0</i><i class="cell r">0</i></div>
  <div class="row" style="top:208px">Kanji ⇒ Kun (94)<i class="cell g">94</i><i class="cell gr">0</i><i class="cell b">0</i><i class="cell r">0</i></div>
  <div class="row" style="top:238px">Kun ⇒ Kanji (94)<i class="cell g">94</i><i class="cell gr">0</i><i class="cell b">0</i><i class="cell r">0</i></div>
  <div class="row" style="top:268px">Word ⇒ Reading (582)<i class="cell g">582</i><i class="cell gr">0</i><i class="cell b">0</i><i class="cell r">0</i></div>
  <div class="row" style="top:298px">Reading ⇒ Word (582)<i class="cell g">582</i><i class="cell gr">0</i><i class="cell b">0</i><i class="cell r">0</i></div>
  <div class="row" style="top:328px">Writing (103)<i class="cell g">103</i><i class="cell gr">0</i><i class="cell b">0</i><i class="cell r">0</i></div>
  <div class="row" style="top:358px;border:0">ALL TESTS (1867)
    <span class="abs" style="left:118px;font-weight:400;color:#888;font-size:7px">1867</span>
    <span class="abs c-green" style="left:164px;font-size:7px">0</span>
    <span class="abs c-blue" style="left:194px;font-size:7px">0</span>
    <span class="abs c-red" style="left:224px;font-size:7px">0</span></div>
  <div class="bottombar" style="background:#f7f7f7">
    <div class="burger"></div>
    <div style="margin-left:auto;display:flex">
      <div class="tool"><svg width="11" height="11" viewBox="0 0 12 12"><circle cx="6" cy="6" r="3.2" fill="none" stroke="#bbb" stroke-width="2.4" stroke-dasharray="2 1.3"/><circle cx="6" cy="6" r="1.3" fill="#bbb"/></svg>SETTINGS</div>
      <div class="tool"><svg width="11" height="11" viewBox="0 0 12 12"><circle cx="7" cy="5" r="3.6" fill="none" stroke="#bbb" stroke-width="1.3"/><path d="M4.3 7.8 1 11" stroke="#bbb" stroke-width="1.5"/></svg>SEARCH</div>
      <div class="tool"><svg width="11" height="11" viewBox="0 0 12 12"><circle cx="6" cy="6" r="4.6" fill="none" stroke="#bbb" stroke-width="1.2"/><circle cx="6" cy="6" r="1.8" fill="#bbb"/></svg>GAMES</div>
      <div class="tool"><svg width="11" height="11" viewBox="0 0 12 12"><path d="M2.5 1h5l2.5 2.5V11h-7.5z" fill="#bbb"/></svg>PAPER</div>
    </div>
  </div>
</section>

<!-- 2 Writing test -->
<section class="screen" style="left:316px;top:110px">
  <div class="status"><span>●●●●○ Carrier</span><span>5:30PM</span><span>100%<i class="bat"></i></span></div>
  <div class="score">
    <div><div class="lab c-dark">REMAINING</div><div class="num c-dark">102</div></div>
    <div><div class="lab c-green">CORRECT</div><div class="num c-green">0</div></div>
    <div><div class="lab c-red">WRONG</div><div class="num c-red">1</div></div>
  </div>
  <div class="card" style="top:79px;height:296px">
    <span class="star" style="right:8px;top:6px">☆</span>
    <div class="abs" style="top:10px;width:100%;text-align:center;font-size:25px;font-weight:300;color:var(--ink)">fire</div>
    <div class="abs jp" style="top:46px;width:100%;text-align:center;font-size:7px;color:#aaa">カ、ひ</div>
    <div class="board" style="left:10px;top:70px;width:210px;height:210px"><div class="big" style="font-size:180px;font-weight:700">火</div></div>
  </div>
  <div class="bottombar" style="background:#fff"><div class="burger"></div><span style="margin-left:auto">NEXT ›</span></div>
</section>

<!-- 3 Writing feedback -->
<section class="screen" style="left:602px;top:110px">
  <div class="status"><span>●●●●○ Carrier</span><span>5:30PM</span><span>100%<i class="bat"></i></span></div>
  <div class="score">
    <div><div class="lab">&nbsp;</div><div class="num c-blue">0</div></div>
    <div><div class="lab c-green">CORRECT</div><div class="num c-green">0</div></div>
    <div><div class="lab c-red">WRONG</div><div class="num c-red">1</div></div>
  </div>
  <div class="card" style="top:79px;height:296px">
    <div class="abs c-green" style="top:4px;width:100%;text-align:center;font-size:9px">✔</div>
    <div class="abs jp" style="top:12px;width:100%;text-align:center;font-size:24px;color:var(--ink)">江</div>
    <div class="abs" style="top:46px;width:100%;text-align:center;font-size:7px;color:#aaa">creek</div>
    <svg class="abs" style="right:16px;top:78px" width="9" height="10" viewBox="0 0 9 10"><path d="M1 2h7M3 2V1h3v1M2 3h5l-.5 7h-4z" fill="#ccc" stroke="#ccc" stroke-width=".6"/></svg>
    <div class="board" style="left:10px;top:70px;width:210px;height:210px"><div class="big" style="font-size:170px;font-weight:700">江</div></div>
  </div>
  <div class="bottombar" style="background:#fff"><div class="burger"></div>
    <span class="jp" style="margin-left:auto;width:38px;height:38px;border-radius:50%;border:1.5px solid var(--green);display:flex;align-items:center;justify-content:center;font-size:18px;font-weight:400;color:#333">江</span>
    <span class="jp" style="margin-left:6px;width:38px;height:38px;border-radius:50%;border:1.5px solid var(--blue);display:flex;align-items:center;justify-content:center;font-size:18px;font-weight:400;color:#333">江</span>
  </div>
</section>

<!-- 4 Game -->
<section class="screen" style="left:888px;top:110px">
  <div class="status"><span>●●●●○ Carrier</span><span>5:30PM</span><span>100%<i class="bat"></i></span></div>
  <div class="score">
    <div class="c-red"><div class="lab">LIVES</div><div class="num">3</div><div class="sub">Level N5</div></div>
    <div class="c-blue"><div class="lab">SCORE</div><div class="num">0</div><div class="sub">Highscore: 8</div></div>
    <div class="c-yellow"><div class="lab">COINS</div><div class="num">12</div><div class="sub">&nbsp;</div></div>
  </div>
  <div class="card" style="top:89px;height:276px">
    <div class="abs jp" style="top:14px;width:100%;text-align:center;font-size:25px;color:var(--ink)">ハク、びゃく</div>
    <div class="gamegrid" style="left:10px;top:56px">
      <div class="off">国</div><div class="off">石</div><div>年</div>
      <div>七</div><div class="off">外</div><div class="off">毎</div>
      <div>一</div><div>百</div><div class="off">新</div>
    </div>
  </div>
  <div class="bottombar" style="background:#fff;height:44px"><div class="burger"></div>
    <div style="margin-left:auto;display:flex;gap:8px">
      <div class="coin">LEVEL<br>UP</div><div class="coin off">LIVE+<br>-24</div><div class="coin">SPLIT<br>-8</div><div class="coin">HINT<br>-4</div>
    </div>
  </div>
</section>

<!-- 5 Reading test -->
<section class="screen" style="left:30px;top:644px">
  <div class="status"><span>●●●●○ Carrier</span><span>5:30PM</span><span>100%<i class="bat"></i></span></div>
  <div class="score">
    <div><div class="lab c-dark">REMAINING</div><div class="num c-dark">102</div></div>
    <div><div class="lab c-green">CORRECT</div><div class="num c-green">0</div></div>
    <div><div class="lab c-red">WRONG</div><div class="num c-red">1</div></div>
  </div>
  <div class="card" style="top:80px;height:290px">
    <span class="star" style="right:8px;top:6px">☆</span>
    <div class="abs jp" style="top:12px;width:100%;text-align:center;font-size:26px;color:var(--ink)">名</div>
    <div class="abs jp" style="top:48px;width:100%;text-align:center;font-size:7px;color:#aaa">メイ、ミョウ、な</div>
    <div class="answers">
      <div>seven</div><div class="bad"><b>✕</b>person</div><div>long</div>
      <div class="good"><b>✔</b>name</div><div>come</div><div>may</div>
      <div>write</div><div>in</div><div>station</div>
    </div>
  </div>
  <div class="bottombar" style="background:#fff"><div class="burger"></div><span style="margin-left:auto;color:#999;font-weight:400">SKIP ›</span></div>
</section>

<!-- 6 Search -->
<section class="screen" style="left:316px;top:644px;background:#fff">
  <div class="status"><span>●●●●○ Carrier</span><span>5:30PM</span><span>100%<i class="bat"></i></span></div>
  <div class="abs" style="left:10px;right:10px;top:30px;height:22px;border-bottom:1px solid #ccc;font-size:8.5px;font-style:italic;color:#777;display:flex;align-items:center;gap:4px">
    <svg width="9" height="9" viewBox="0 0 12 12"><circle cx="7" cy="5" r="3.6" fill="none" stroke="#555" stroke-width="1.4"/><path d="M4.3 7.8 1 11" stroke="#555" stroke-width="1.6"/></svg>Search...</div>
  <div class="abs" style="left:10px;top:74px;font-size:7.5px;color:#999">2278 Entries Found:</div>
  <div class="abs" style="left:0;top:88px;width:100%;border-top:1px solid var(--line)"></div>
  <div class="entry" style="top:89px"><span class="kana">あ</span><span class="rom">a</span><span class="dots">●●●</span><span class="type">Hiragana</span><span class="lvl">K</span><span class="st">☆</span></div>
  <div class="entry" style="top:137px"><span class="kana">い</span><span class="rom">i</span><span class="dots">●●●</span><span class="type">Hiragana</span><span class="lvl">K</span><span class="st">☆</span></div>
  <div class="entry" style="top:185px"><span class="kana">う</span><span class="rom">u</span><span class="dots">●●●</span><span class="type">Hiragana</span><span class="lvl">K</span><span class="st">☆</span></div>
  <div class="entry" style="top:233px"><span class="kana">え</span><span class="rom">e</span><span class="dots">●●●</span><span class="type">Hiragana</span></div>
  <div class="entry" style="top:281px"><span class="kana">お</span><span class="rom">o</span><span class="dots">●●●</span><span class="type">Hiragana</span></div>
  <div class="entry" style="top:329px"><span class="kana">か</span><span class="rom">ka</span><span class="dots">●●●</span><span class="type">Hiragana</span></div>
  <div class="entry" style="top:377px"><span class="kana">が</span><span class="rom">ga</span><span class="dots">●●●</span><span class="type">Hiragana</span></div>
  <div class="popup">
    <div class="btn">PRACTICE WRITING ›</div>
    <div class="lab">MARK &amp; UNMARK TESTS:</div>
    <div><i class="dot" style="background:var(--olive)"></i><i class="dot" style="background:var(--orange)"></i><i class="dot" style="background:var(--purple)"></i><i class="dot" style="background:#bdbdbd"></i></div>
    <div class="lab">MARK &amp; UNMARK KANJIS:</div>
    <div style="font-size:22px;line-height:22px"><span style="color:#111">★</span> <span style="color:#ccc">☆</span></div>
  </div>
  <div class="bottombar" style="background:#fff;border-top:1px solid var(--line);height:30px"><div class="burger"></div><span style="margin-left:10px;color:#888">?</span><span style="margin-left:auto;font-size:7.5px">TOOLS ⌃</span></div>
</section>

<!-- 7 Settings -->
<section class="screen" style="left:602px;top:644px">
  <div class="status"><span>●●●●○ Carrier</span><span>5:30PM</span><span>100%<i class="bat"></i></span></div>
  <div class="hdr">SETTINGS<div class="burger abs" style="left:10px;top:13px"></div></div>
  <div class="set-lab" style="top:72px">Group Tests by:</div>
  <div class="seg" style="top:88px"><span class="sel">JLPT LEVEL</span><span>SCHOOL YEAR</span></div>
  <div class="set-lab" style="top:130px">Size of Answer Grid:</div>
  <div class="seg" style="top:146px"><span class="sel">3 X 3</span><span>4 X 4</span></div>
  <div class="set-lab" style="top:188px">Show Meaning in Tests:</div>
  <div class="seg" style="top:204px"><span>NEVER</span><span class="sel">CLASSIC</span><span>ALWAYS</span></div>
  <div class="set-lab" style="top:246px">Show Pattern in Writing Tests:</div>
  <div class="seg" style="top:262px"><span>NEVER</span><span class="sel">FIRST TESTS</span><span>ALWAYS</span></div>
  <div class="set-lab" style="top:304px">Tests used in Game:</div>
  <div class="seg" style="top:320px"><span>MEANING</span><span>READING</span><span class="sel">BOTH</span></div>
  <div class="set-lab" style="top:362px">Feedback:</div>
  <div class="seg" style="top:378px"><span>RATE</span><span>EMAIL</span></div>
  <div class="abs" style="left:10px;right:10px;top:420px;border-top:1px solid #ddd;padding-top:5px;text-align:center;font-size:6.5px;font-style:italic;color:#888">many thanks to lexidex.org and strokebase.net</div>
</section>

<!-- 8 Detailed information -->
<section class="screen" style="left:888px;top:644px">
  <div class="status"><span>●●●●○ Carrier</span><span>5:30PM</span><span>100%<i class="bat"></i></span></div>
  <div class="hdr">DETAILED INFORMATION<div class="burger abs" style="left:10px;top:13px"></div><span class="abs" style="right:10px;font-weight:600;color:#333">‹ BACK</span></div>
  <div class="abs" style="top:52px;left:0;width:100%;height:75px;background:#fff;border-bottom:1px solid var(--line);text-align:center">
    <div class="jp" style="font-size:6.5px;color:#aaa;margin-top:8px">がいこくご</div>
    <div class="jp" style="font-size:28px;color:#999;line-height:32px">外国語</div>
    <div style="font-size:7.5px;color:#aaa">foreign language</div>
  </div>
  <div class="drow" style="top:128px;height:46px"><span style="left:8px;top:8px">【語】word</span><span class="jp" style="left:96px;top:8px">ゴ</span><span class="jp" style="left:96px;top:22px">かた<b class="red" style="font-weight:400">る</b>、かた<b class="red" style="font-weight:400">らう</b></span><span style="right:10px;top:8px">N5</span></div>
  <div class="sect" style="top:188px">Non-trrival Components of Kanji 語:</div>
  <div class="drow" style="top:204px;height:26px"><span style="left:8px;top:7px">【言】say</span><span class="jp" style="left:96px;top:7px">ゲン、ゴン</span><span class="jp" style="left:156px;top:7px">い、こと</span><span style="right:10px;top:7px">N5</span></div>
  <div class="drow" style="top:230px;height:26px"><span style="left:8px;top:7px">【五】five</span><span class="jp" style="left:96px;top:7px">ゴ</span><span class="jp" style="left:156px;top:7px">いつ-</span><span style="right:10px;top:7px">N5</span></div>
  <div class="sect" style="top:270px">Similar Pronounciation and in Group N5:</div>
  <div class="drow" style="top:286px;height:26px"><span style="left:8px;top:7px">【五】five</span><span class="jp" style="left:96px;top:7px">ゴ</span><span class="jp" style="left:156px;top:7px">いつ-</span><span style="right:10px;top:7px">N5</span></div>
  <div class="drow" style="top:312px;height:26px"><span style="left:8px;top:7px">【午】noon</span><span class="jp" style="left:96px;top:7px">ゴ</span><span style="right:10px;top:7px">N5</span></div>
  <div class="drow" style="top:338px;height:26px"><span style="left:8px;top:7px">【後】behind</span><span class="jp" style="left:96px;top:7px">ゴ、こう</span><span class="jp" style="left:156px;top:7px">あと、うし-</span><span style="right:10px;top:7px">N5</span></div>
  <div class="sect" style="top:378px">Example Words for 語 used in Tests:</div>
  <div class="drow" style="top:394px;height:40px"><span class="jp" style="left:8px;top:6px">【言語】げんご</span><span class="red" style="left:8px;top:21px">language</span></div>
  <div class="drow" style="top:434px;height:40px"><span class="jp" style="left:8px;top:6px">【用語】ようご</span><span class="red" style="left:8px;top:21px">terms, terminology</span></div>
</section>

</body>
</html>
```